Velmora Investment Management Needs Door Wording Design

We need someone to put together a design for our glass front doors (2).

The words could be, but aren't limited to, as follows:

"100
Serenely Restorative Bodywork
*Ring Bell"

and

"200 & 300
Velmora Investment Management inc.
*Ring Bell"

The design should be clean, subtle and professional. It is a simple mainly glass door with a black frame. Our website is www.velmorainvest.ca for a more detailed description of what we do. The adjacent business would also be involved, as per the wording of the Serenely Restorative Bodywork.

We are looking for something to bring out the wording on the door (there is currently a piece of paper printed and taped to the inside).

Dimensions of the window are 47 inches x 23 inches.

Thanks!

Colors
000000
ffffff

Requirements
Must have
• The previous words
Nice to have
• Creative flair, taking into consideration the nature of our business (Investment Management)

```html
<!DOCTYPE html>
<html lang="en">
<head>
<meta charset="utf-8">
<title>Serenely Restorative Bodywork – Door Panel</title>
<link href="https://fonts.googleapis.com/css2?family=Arimo:wght@700&family=Bebas+Neue&display=swap" rel="stylesheet">
<style>
  :root {
    --ink: #000000;
    --paper: #ffffff;
  }
  html, body {
    margin: 0;
    padding: 0;
    width: 1200px;
    height: 2453px;
    overflow: hidden;
    background: var(--ink);
  }
  .door-panel {
    position: relative;
    width: 1200px;
    height: 2453px;
    background: var(--ink);
    color: var(--paper);
    font-family: "Arimo", Arial, sans-serif;
    font-weight: 700;
  }
  .greeting {
    position: absolute;
    left: 124px;
    top: 588px;
    margin: 0;
    font-size: 205px;
    line-height: 1;
    letter-spacing: 12px;
  }
  .business-name {
    position: absolute;
    left: 129px;
    top: 856px;
    margin: 0;
    font-size: 125px;
    line-height: 123px;
    letter-spacing: 1px;
  }
  .business-name .name-line {
    display: block;
  }
  .business-name .suffix {
    display: block;
    font-size: 70px;
    line-height: 105px;
    letter-spacing: 0.5px;
  }
  .wave-rule {
    position: absolute;
    left: 116px;
    top: 1248px;
    width: 968px;
    height: 48px;
  }
  .contact {
    position: absolute;
    left: 129px;
    top: 1344px;
    margin: 0;
    font-size: 82px;
    line-height: 1;
    letter-spacing: 1px;
    white-space: pre;
  }
  .bell-icon {
    position: absolute;
    left: 140px;
    top: 2084px;
    width: 180px;
    height: 200px;
  }
  .bell-notice {
    position: absolute;
    left: 399px;
    top: 2104px;
    margin: 0;
    font-family: "Bebas Neue", "Arial Narrow", sans-serif;
    font-weight: 400;
    font-size: 94px;
    line-height: 96px;
    letter-spacing: 0.5px;
  }
</style>
</head>
<body>
  <main class="door-panel">
    <h1 class="greeting">welcome</h1>
    <h2 class="business-name">
      <span class="name-line">serenely</span>
      <span class="name-line">restorative</span>
      <span class="suffix">bodywork company inc.</span>
    </h2>
    <svg class="wave-rule" viewBox="0 0 968 48" aria-hidden="true">
      <path d="M4 34 Q32 12 62 22 T122 22 T182 22 T242 22 T302 22 T362 22 T422 22 T482 22 T542 22 T602 22 T662 22 T722 22 T782 22 T842 22 T902 22 Q938 40 964 36"
            fill="none" stroke="var(--paper)" stroke-width="7" stroke-linecap="round"/>
    </svg>
    <p class="contact">Call:  (780) 555-0142</p>
    <svg class="bell-icon" viewBox="0 0 180 200" aria-hidden="true">
      <g fill="none" stroke="var(--paper)" stroke-width="12" stroke-linecap="round" stroke-linejoin="round" transform="rotate(-40 80 90)">
        <path d="M80 16 v12"/>
        <path d="M36 128 C42 104 36 70 54 50 C68 34 92 34 106 50 C124 70 118 104 124 128 Z"/>
        <path d="M20 130 H140"/>
      </g>
      <g fill="none" stroke="var(--paper)" stroke-width="12" stroke-linecap="round">
        <path d="M112 150 a16 16 0 0 0 18 -18"/>
        <path d="M100 172 a40 40 0 0 0 50 -48"/>
        <path d="M90 194 a64 64 0 0 0 82 -76"/>
      </g>
    </svg>
    <p class="bell-notice">Please ring the<br>doorbell if locked</p>
  </main>
</body>
</html>
```